DERMATOLOGY SERVICES ADDING CARE FOR sKIN, HAIR AND NAILS

postcard TO BE DISTRIBUTED TO RURAL COMMUNITY. medical CLINIC EXPANDING AND ADDING DERMATOLOGIST. TREATMENT OF skin PROBLEMS LIKE RASHES, SABIES, SKIN CANCERS, ROSACEA, PSORIASIS, ECZEMA, WOUND CARE, ACNE, ANTI-AGING AND OTHER BREAKDOWN OF SKIN.
SERVICES INCLUDED PLEASE SEE ATTACHED DOCUMENT
Updates

Project Deadline Extended
Reason: The designs we got few designers that sent designs and they are not what we want. We need to have more time

Target Market(s)

rural COMMUNITY

Industry/Entity Type

Medical

Font styles to use
Other font styles liked:
• LET DESIGNER CHOOSE

Requirements
Must have
• SKIN PROBLEMS AND DISORDERS MENTIONED IN THE ATTACHED FILES
• MEDICAL PROFESSION
• ADDRESS PHONE NUMBERS
• 482 N Larkin Avenue Wauchula, Florida 33870
• phone # 863-555-0182
• Marlow Tenbury Inc expanding its services
• mOST INSURANCE ACCEPTED INCLUDING MEDICARE
Nice to have
• ADD A LOGO
Should not have
• This is a US postcard to be left in restaurants, doctors offices RV park. No stamp or address line in the back

```html
<!DOCTYPE html>
<html lang="en">
<head>
<meta charset="utf-8">
<title>Dermatologist Now in Wauchula – Postcard</title>
<link href="https://fonts.googleapis.com/css2?family=Oswald:wght@400;500;600&family=Open+Sans:wght@400;600;700&display=swap" rel="stylesheet">
<style>
  :root {
    --teal: #49c1b8;
    --teal-dark: #2f9e96;
    --ink: #2b2d31;
    --ink-soft: #3a3d42;
    --white: #ffffff;
    --paper: #e9eaec;
    --skin-light: #f3e3da;
    --skin-mid: #d9b9a8;
    --text-dark: #30343a;
    --text-muted: #5b6068;
  }
  * { box-sizing: border-box; margin: 0; padding: 0; }
  html, body { width: 900px; height: 1200px; overflow: hidden; }
  body {
    background: var(--paper);
    font-family: "Open Sans", Arial, sans-serif;
    position: relative;
  }
  .card {
    position: absolute;
    left: 50px;
    width: 800px;
    height: 540px;
    background: var(--white);
    overflow: hidden;
    box-shadow: 0 4px 14px rgba(0,0,0,.18);
  }
  .card--front { top: 45px; }
  .card--back { top: 615px; }
  .heading-font { font-family: "Oswald", "Arial Narrow", sans-serif; text-transform: uppercase; }

  /* ---------- front ---------- */
  .hero-photo {
    position: absolute; left: 0; top: 0; width: 450px; height: 330px;
    background: linear-gradient(135deg, #f6f1ee 0%, var(--skin-light) 45%, #c9d3dc 100%);
    clip-path: polygon(0 0, 100% 0, 92% 100%, 0 100%);
  }
  .headline-box {
    position: absolute; left: 430px; top: 22px; width: 370px; height: 98px;
    background: var(--teal);
    padding: 10px 18px 0 30px;
    clip-path: polygon(6% 0, 100% 0, 100% 100%, 0 100%);
  }
  .headline-box .line-1 { color: var(--white); font-size: 34px; font-weight: 500; line-height: 1.1; }
  .headline-box .line-2 { color: var(--ink); font-size: 27px; font-weight: 500; line-height: 1.2; }
  .service-list {
    position: absolute; left: 445px; top: 148px; width: 200px;
    list-style: none; color: var(--text-dark); font-size: 14px; line-height: 1.75; font-weight: 600;
  }
  .service-list li::before {
    content: ""; display: inline-block; width: 7px; height: 7px; border-radius: 50%;
    background: var(--teal); margin-right: 8px; vertical-align: middle;
  }
  .portrait-photo {
    position: absolute; left: 650px; top: 142px; width: 138px; height: 164px;
    border-radius: 16px;
    background: radial-gradient(circle at 50% 40%, var(--skin-light), var(--skin-mid) 70%, #b7c7d0 100%);
    border: 4px solid var(--teal);
  }
  .location-band {
    position: absolute; left: 0; top: 335px; width: 440px; height: 147px;
    background: var(--ink);
    padding: 0 26px;
    border-top: 6px solid var(--teal);
    display: flex; flex-direction: column; justify-content: center;
  }
  .location-band .title { color: var(--teal); font-size: 36px; font-weight: 600; line-height: 1.05; }
  .location-band .place { color: var(--white); font-size: 28px; font-weight: 400; line-height: 1.2; }
  .contact-band {
    position: absolute; left: 440px; top: 330px; width: 360px; height: 62px;
    background: var(--ink);
    color: var(--white); font-size: 26px; font-weight: 500;
    display: flex; align-items: center; justify-content: center;
  }
  .thumb-row {
    position: absolute; left: 440px; top: 392px; width: 360px; height: 90px;
    background: var(--teal);
    display: flex; gap: 16px; align-items: center; justify-content: center;
  }
  .thumb-photo {
    width: 150px; height: 68px; border-radius: 10px; border: 3px solid var(--white);
    background: linear-gradient(120deg, #f4ebe6, var(--skin-mid));
  }
  .web-strip {
    position: absolute; left: 0; top: 482px; width: 800px; height: 58px;
    background: var(--ink-soft);
    color: var(--white); font-size: 18px; font-weight: 400; letter-spacing: .5px;
    display: flex; align-items: center; padding-left: 26px;
  }

  /* ---------- back ---------- */
  .back-panel {
    position: absolute; left: 0; top: 0; width: 400px; height: 540px;
    background: var(--ink);
  }
  .back-title { position: absolute; left: 24px; top: 20px; }
  .back-title .title { color: var(--teal); font-size: 36px; font-weight: 600; line-height: 1.05; }
  .back-title .place { color: var(--white); font-size: 28px; line-height: 1.2; }
  .lips-photo {
    position: absolute; left: 0; top: 118px; width: 400px; height: 190px;
    background: linear-gradient(90deg, #f7efea 0%, var(--skin-light) 50%, #d39a93 100%);
    border-top: 6px solid var(--teal); border-bottom: 6px solid var(--teal);
  }
  .benefit-list {
    position: absolute; left: 24px; top: 330px; width: 340px;
    list-style: none; color: var(--white); font-size: 14px; line-height: 1.55;
  }
  .benefit-list li { padding-left: 18px; position: relative; margin-bottom: 4px; }
  .benefit-list li::before {
    content: ""; position: absolute; left: 0; top: 7px; width: 8px; height: 8px; background: var(--teal);
  }
  .back-web {
    position: absolute; left: 24px; bottom: 24px;
    color: var(--white); font-size: 18px; letter-spacing: .5px;
  }
  .info-side {
    position: absolute; left: 400px; top: 0; width: 400px; height: 540px;
    background: var(--white);
    padding: 40px 36px;
    display: flex; flex-direction: column;
  }
  .clinic-name { color: var(--ink); font-size: 34px; font-weight: 600; line-height: 1.1; }
  .clinic-tagline { color: var(--teal-dark); font-size: 20px; font-weight: 500; margin-top: 4px; }
  .info-rule { width: 70px; height: 5px; background: var(--teal); margin: 22px 0 26px; }
  .info-row { display: flex; align-items: flex-start; gap: 14px; margin-bottom: 22px; }
  .info-icon {
    flex: 0 0 38px; width: 38px; height: 38px; border-radius: 50%;
    background: var(--teal); display: flex; align-items: center; justify-content: center;
  }
  .info-text { color: var(--text-dark); font-size: 17px; font-weight: 600; line-height: 1.4; padding-top: 7px; }
  .insurance-note {
    margin-top: auto;
    background: var(--ink); color: var(--white);
    border-left: 6px solid var(--teal);
    padding: 16px 20px;
    font-size: 20px; font-weight: 500; line-height: 1.25;
  }
  .insurance-note .accent { color: var(--teal); }
</style>
</head>
<body>

<section class="card card--front">
  <div class="hero-photo" role="img" aria-label="Dermatologist in gloves examining a patient's face"></div>

  <div class="headline-box heading-font">
    <div class="line-1">Treat skin with care</div>
    <div class="line-2">With our clinical touch</div>
  </div>

  <ul class="service-list">
    <li>Mole and Skin Tag removal</li>
    <li>Treatment of various skin</li>
    <li>Skin exams</li>
    <li>Skin Disorders</li>
    <li>Skin Biopsies</li>
    <li>Hair and nail disease</li>
  </ul>

  <div class="portrait-photo" role="img" aria-label="Patient receiving a cosmetic skin treatment"></div>

  <div class="location-band heading-font">
    <div class="title">Dermatologist now</div>
    <div class="place">In Wauchula, Florida</div>
  </div>

  <div class="contact-band heading-font">Contact us at - 863-555-0182</div>

  <div class="thumb-row">
    <div class="thumb-photo" role="img" aria-label="Skin care treatment in progress"></div>
    <div class="thumb-photo" role="img" aria-label="Facial treatment at the clinic"></div>
  </div>

  <div class="web-strip heading-font">Visit us at- www.ourwebsite.com</div>
</section>

<section class="card card--back">
  <div class="back-panel">
    <div class="back-title heading-font">
      <div class="title">Dermatologist now</div>
      <div class="place">In Wauchula, Florida</div>
    </div>
    <div class="lips-photo" role="img" aria-label="Close-up of a gloved hand giving a cosmetic lip treatment"></div>
    <ul class="benefit-list">
      <li>No need to drive</li>
      <li>Care in your community</li>
      <li>Treat skin problems like skin cancers, rosacea, psoriasis, eczema, wound care and other breakdowns</li>
    </ul>
    <div class="back-web heading-font">Visit us at- www.ourwebsite.com</div>
  </div>

  <div class="info-side">
    <div class="clinic-name heading-font">Marlow Tenbury Inc</div>
    <div class="clinic-tagline heading-font">Expanding its services</div>
    <div class="info-rule"></div>

    <div class="info-row">
      <span class="info-icon">
        <svg width="18" height="18" viewBox="0 0 24 24" aria-hidden="true"><path fill="#fff" d="M12 2a7 7 0 0 0-7 7c0 5 7 13 7 13s7-8 7-13a7 7 0 0 0-7-7zm0 9.5A2.5 2.5 0 1 1 12 6.5a2.5 2.5 0 0 1 0 5z"/></svg>
      </span>
      <span class="info-text">482 N Larkin Avenue<br>Wauchula, Florida 33870</span>
    </div>

    <div class="info-row">
      <span class="info-icon">
        <svg width="18" height="18" viewBox="0 0 24 24" aria-hidden="true"><path fill="#fff" d="M6.6 10.8a15 15 0 0 0 6.6 6.6l2.2-2.2a1 1 0 0 1 1-.25 11.4 11.4 0 0 0 3.6.57 1 1 0 0 1 1 1V20a1 1 0 0 1-1 1A17 17 0 0 1 3 4a1 1 0 0 1 1-1h3.5a1 1 0 0 1 1 1c0 1.25.2 2.45.57 3.57a1 1 0 0 1-.25 1z"/></svg>
      </span>
      <span class="info-text">863-555-0182</span>
    </div>

    <div class="insurance-note heading-font">
      Most insurance accepted<br><span class="accent">including Medicare</span>
    </div>
  </div>
</section>

</body>
</html>
```